Association qui souhaite améliorer l'accès aux personnes en situation de handicap

Nous sommes une association qui a pour objectif d'améliorer l'accessibilité, augmenter l'offre des activités réalisables dans notre région touristique.
Nous souhaitons réaliser un site internet afin de pouvoir communiquer sur notre association. Nous avons déjà conçu notre flyer sur Graphivolte. Nous souhaiterions une base graphique se rapportant à celui-ci. C'est possible de tout retravailler mais nous souhaitons tout de même retrouver la charte graphique ou code couleur du flyer.
Il nous faudrait quelques pages:
- 1 page : Acceuil / Présentation (Home), Il y aurait le descriptif de l'association, avec ses objectifs à +/- moyen terme
- 1 page : Nos réalisations, celle-ci présenterait les éléments que nous avons réalisés avec des zones de textes et des images classées chronologiquement au fur et à mesure des nouveautés
- 1 page : Media, comme la précédente, mais ou on pourrait voir ou lire sur les divers médias qui parlent de nous
- 1 page : Evenements : c'est une page pour présenter divers activités que nous allons organiser
- 1 page : Contact qui indique comment nous contacter et avec la présentation des 5 ou 6 membres du comité
- 1 link donate : qui arrive sur un formulaire de donnée que l'on pourra faire évoluer sur un système de payement par la suite. Cette bannière doit se retrouver sur toutes les pages
Il est nécessaire que se design puisse être transféré sur une lecture sur téléphone mobile
Personnes en situation de handicap
Associatif
Coded - Design and coding required
5+ page

```html
<!DOCTYPE html>
<html lang="fr">
<head>
<meta charset="utf-8">
<title>Portail Ensemble Association</title>
<link href="https://fonts.googleapis.com/css2?family=Poppins:wght@400;500;600;700;800;900&display=swap" rel="stylesheet">
<style>
:root{
  --red:#c1161f;
  --dark:#2f3a42;
  --text:#3b4248;
  --muted:#6b7177;
  --line:#dde0e3;
  --white:#ffffff;
  --grey:#ececec;
}
*{margin:0;padding:0;box-sizing:border-box}
html,body{width:1200px;height:3828px;overflow:hidden}
body{position:relative;font-family:'Poppins',sans-serif;color:var(--text);background:var(--white)}
.abs{position:absolute}
.photo{position:absolute}
/* header */
.site-header{position:absolute;left:0;top:0;width:1200px;height:89px;background:var(--white);z-index:5}
.brand{position:absolute;left:89px;top:26px;display:flex;align-items:center;gap:10px}
.brand-mark{width:26px;height:26px;background:var(--red)}
.brand-name{font-weight:700;font-size:19px;line-height:19px;color:var(--red);text-transform:uppercase}
.main-nav{position:absolute;left:470px;top:0;display:flex;height:89px}
.main-nav a{font-size:13.5px;font-weight:500;color:var(--text);text-decoration:none;padding:36px 15px 0;text-transform:uppercase}
.main-nav a.active{color:var(--red);border-top:3px solid var(--red);padding-top:33px}
.btn-donate-nav{position:absolute;left:1004px;top:24px;width:106px;height:40px;border:2px solid var(--red);color:var(--red);font-weight:600;font-size:14px;display:flex;align-items:center;justify-content:center}
/* hero */
.hero-photo{left:0;top:89px;width:1200px;height:840px;background:linear-gradient(100deg,#5d6751 0%,#8d917d 35%,#a7a89a 55%,#6f735d 80%,#434a38 100%)}
.hero-title{left:120px;top:220px;font-size:72px;font-weight:800;line-height:68px;color:var(--white)}
.hero-sub{left:120px;top:380px;width:460px;font-size:16px;line-height:27px;color:var(--white);font-weight:500}
.btn-solid{position:absolute;background:var(--red);color:var(--white);font-weight:600;font-size:14px;display:flex;align-items:center;justify-content:center;text-transform:uppercase}
.btn-outline{position:absolute;border:2px solid var(--red);color:var(--red);font-weight:600;font-size:14px;display:flex;align-items:center;justify-content:center;text-transform:uppercase}
/* sections */
.section-title{position:absolute;font-size:37px;font-weight:800;line-height:45px;color:var(--dark)}
.title-rule{position:absolute;height:2px;background:var(--line)}
.body-copy{position:absolute;font-size:14.5px;line-height:25px;color:var(--muted)}
/* events */
.event-card{position:absolute;top:2624px;width:295px;height:398px;background:var(--white);box-shadow:0 6px 24px rgba(0,0,0,.10)}
.event-img{height:208px}
.event-date{position:absolute;left:29px;top:231px;font-size:11px;color:#9a9fa4}
.event-title{position:absolute;left:29px;top:256px;font-size:14px;font-weight:600;color:var(--dark)}
.event-text{position:absolute;left:29px;top:285px;width:238px;font-size:12.5px;line-height:18px;color:var(--muted)}
.event-rule{position:absolute;left:29px;right:29px;top:350px;height:1px;background:var(--line)}
.event-more{position:absolute;left:0;right:0;top:367px;text-align:center;font-size:12px;font-weight:600;color:var(--red)}
/* newsletter */
.newsletter{left:190px;top:3135px;width:823px;height:188px;background:var(--red);z-index:3}
.newsletter h2{position:absolute;left:0;right:0;top:38px;text-align:center;color:var(--white);font-size:36px;font-weight:800}
.news-form{position:absolute;left:78px;top:90px;width:645px;height:50px;background:var(--white);display:flex;align-items:center}
.news-form span{flex:1;font-size:13px;color:#8c9196;padding-left:42px}
.news-btn{width:110px;height:44px;margin-right:3px;background:var(--dark);color:var(--white);font-size:13px;font-weight:600;display:flex;align-items:center;justify-content:center}
/* footer */
.footer-col h3{font-size:19px;font-weight:700;color:var(--white);margin-bottom:18px}
.footer-col li{list-style:none;font-size:13px;color:#c7ccd0;line-height:31px}
.footer-col li::before{content:"›";margin-right:8px;color:#8a939a}
.contact-item{position:absolute;font-size:13px;line-height:19px;color:#c7ccd0;padding-left:22px}
.contact-item svg{position:absolute;left:0;top:2px}
.social{position:absolute;top:3621px;width:48px;height:48px;border-radius:50%;background:#3c474f}
.copyright{left:0;right:0;top:3787px;text-align:center;font-size:13px;color:var(--white);font-weight:500}
</style>
</head>
<body>

<header class="site-header">
  <div class="brand"><span class="brand-mark"></span><span class="brand-name">Portail Ensemble</span></div>
  <nav class="main-nav">
    <a class="active">Home</a><a>Our Achievements</a><a>About Us</a><a>Events</a><a>Contact</a>
  </nav>
  <div class="btn-donate-nav">DONATE</div>
</header>

<!-- hero -->
<div class="photo hero-photo" role="img" aria-label="Photo d'une personne âgée en fauteuil roulant rouge sur un chemin de jardin"></div>
<svg class="abs" style="left:0;top:89px" width="1200" height="860" viewBox="0 89 1200 860">
  <polygon points="0,535 729,910 1200,632 1200,949 0,949" fill="#ffffff"/>
  <polygon points="729,925 1200,632 1200,700" fill="#c1161f"/>
</svg>
<h1 class="abs hero-title">Portail<br>Ensemble</h1>
<p class="abs hero-sub">Des amis habitant la région qui ont à cœur de rendre Région Dents du Midi la plus accessible...</p>
<div class="btn-solid" style="left:120px;top:453px;width:148px;height:47px">Donate Now</div>

<!-- about -->
<svg class="abs" style="left:80px;top:720px" width="520" height="720" viewBox="80 720 520 720" role="img" aria-label="Photos d'une enfant soufflant un pissenlit et de mains tenant des herbes">
  <polygon points="121,1440 578,1252 578,975 543,975 543,1222 89,1414" fill="#e8e8e8"/>
  <polygon points="89,733 543,980 543,1222 345,1075 89,1140" fill="#5f8a3e"/>
  <polygon points="89,1140 345,1075 543,1222 89,1414" fill="#4a4a4a"/>
</svg>
<h2 class="section-title" style="left:680px;top:998px">About Portail<br>Ensemble Association</h2>
<div class="title-rule" style="left:648px;top:1095px;width:300px"></div>
<p class="body-copy" style="left:680px;top:1114px;width:420px">Des amis habitant la région qui ont à cœur de rendre la Région Dents du Midi la plus accessible possible aux personnes en situation de handicap. Des amis habitant la région qui ont à cœur de rendre la Région Dents du Midi la plus accessible possible aux personnes en...</p>
<div class="btn-outline" style="left:680px;top:1261px;width:124px;height:41px">Read More</div>

<!-- achievements -->
<h2 class="section-title" style="left:87px;top:1543px">Our<br>Achievements</h2>
<div class="title-rule" style="left:55px;top:1638px;width:300px"></div>
<p class="body-copy" style="left:87px;top:1659px;width:300px;font-size:14px;line-height:22.5px">Des amis habitant la région qui ont à cœur de rendre la Région Dents du Midia plus accessible possible aux personnes en situation de handicap des...</p>
<div class="btn-outline" style="left:87px;top:1772px;width:124px;height:40px">View All</div>
<div class="photo" style="left:440px;top:1475px;width:253px;height:375px;background:linear-gradient(160deg,#9aa590,#6c7a4e 55%,#3d4630)" role="img" aria-label="Main touchant de hautes herbes près d'un fauteuil roulant"></div>
<div class="photo" style="left:703px;top:1475px;width:253px;height:375px;background:linear-gradient(180deg,#7a7a7c,#5e5f62 60%,#8a6c5a)" role="img" aria-label="Fillette souriante en fauteuil roulant dans un gymnase"></div>
<div class="photo" style="left:967px;top:1475px;width:233px;height:375px;background:linear-gradient(180deg,#8fa169,#56683a 60%,#3b4532)" role="img" aria-label="Homme malvoyant marchant avec une canne blanche en forêt"></div>

<!-- projects -->
<svg class="abs" style="left:0;top:1855px" width="640" height="700" viewBox="0 1855 640 700">
  <polygon points="0,1860 205,2065 205,2345 0,2552" fill="#c1161f"/>
  <polygon points="342,1933 622,2205 342,2477 70,2205" fill="#ffffff"/>
  <polygon points="342,1941 614,2205 342,2469 78,2205" fill="#5a3d2a" role="img" aria-label="Mains superposées en signe d'unité"/>
</svg>
<h2 class="section-title" style="left:680px;top:1985px">Projects Of The<br>Association</h2>
<div class="title-rule" style="left:648px;top:2082px;width:300px"></div>
<p class="body-copy" style="left:680px;top:2101px;width:420px">Des amis habitant la région qui ont à cœur de rendre la Région Dents du Midi la plus accessible possible aux personnes en situation de handicap. Des amis habitant la région qui ont à cœur de rendre la Région Dents du Midi la plus accessible possible aux personnes en...</p>
<p class="body-copy" style="left:680px;top:2243px;width:380px">Situation de handicap. Des amis habitant la région qui ont à cœur de rendre la Région Dents du Midi la plus accessible possible aux personnes en...</p>
<div class="btn-outline" style="left:680px;top:2345px;width:124px;height:40px">Read More</div>

<!-- events -->
<h2 class="section-title" style="left:0;right:0;top:2515px;text-align:center">Upcoming Events</h2>
<div class="title-rule" style="left:560px;top:2590px;width:80px"></div>

<article class="event-card" style="left:138px">
  <div class="event-img" style="background:linear-gradient(180deg,#9ab0bd,#6f9a3e 60%,#4f7a2a)" role="img" aria-label="Pieds d'une personne en fauteuil roulant sur l'herbe"></div>
  <div class="event-date">25-05-2022</div>
  <div class="event-title">Some blog heading goes here</div>
  <div class="event-text">Aenean sollicitudin lorem quis bibendum auctor nisi elit consequat ipsum, nec sagittis sem...</div>
  <div class="event-rule"></div>
  <div class="event-more">READ MORE</div>
</article>
<article class="event-card" style="left:452px">
  <div class="event-img" style="background:linear-gradient(135deg,#d7b9a4,#b8876a 60%,#8e604a)" role="img" aria-label="Gros plan d'une oreille et d'une main"></div>
  <div class="event-date">25-05-2022</div>
  <div class="event-title">Some blog heading goes here</div>
  <div class="event-text">Aenean sollicitudin lorem quis bibendum auctor nisi elit consequat ipsum, nec sagittis sem...</div>
  <div class="event-rule"></div>
  <div class="event-more">READ MORE</div>
</article>
<article class="event-card" style="left:767px">
  <div class="event-img" style="background:linear-gradient(135deg,#5d6d4c,#a59a8c 55%,#6e7a84)" role="img" aria-label="Père et fils se serrant avec tendresse"></div>
  <div class="event-date">25-05-2022</div>
  <div class="event-title">Some blog heading goes here</div>
  <div class="event-text">Aenean sollicitudin lorem quis bibendum auctor nisi elit consequat ipsum, nec sagittis sem...</div>
  <div class="event-rule"></div>
  <div class="event-more">READ MORE</div>
</article>

<!-- footer background -->
<svg class="abs" style="left:0;top:3300px" width="1200" height="528" viewBox="0 3300 1200 528">
  <polygon points="0,3555 560,3320 1200,3500 1200,3828 0,3828" fill="#d9dcdf"/>
  <polygon points="0,3570 560,3335 1200,3515 1200,3828 0,3828" fill="#2f3a42"/>
</svg>

<!-- newsletter -->
<section class="abs newsletter">
  <h2>Subscribe Newsletter</h2>
  <div class="news-form">
    <svg class="abs" style="left:18px;top:19px" width="16" height="12" viewBox="0 0 16 12"><rect x="0.5" y="0.5" width="15" height="11" fill="none" stroke="#8c9196"/><polyline points="0.5,0.5 8,7 15.5,0.5" fill="none" stroke="#8c9196"/></svg>
    <span>Enter your email address...</span>
    <div class="news-btn">SUBSCRIBE</div>
  </div>
</section>

<!-- footer -->
<div class="abs" style="left:137px;top:3543px;display:flex;align-items:center;gap:10px">
  <span style="width:30px;height:30px;border:3px solid #fff;display:block"></span>
  <span style="font-size:23px;font-weight:700;color:#fff;text-transform:uppercase;line-height:24px">Portail<br>Ensemble</span>
</div>
<div class="social" style="left:154px" role="img" aria-label="Réseau social 1"></div>
<div class="social" style="left:214px" role="img" aria-label="Réseau social 2"></div>
<div class="social" style="left:274px" role="img" aria-label="Réseau social 3"></div>
<div class="social" style="left:332px" role="img" aria-label="Réseau social 4"></div>

<div class="abs footer-col" style="left:471px;top:3466px">
  <h3>Quick Links</h3>
  <ul><li>Home</li><li>Our achievements</li><li>About us</li><li>Events</li><li>Contact</li><li>Donate Now</li></ul>
</div>
<div class="abs footer-col" style="left:668px;top:3466px">
  <h3>Information</h3>
  <ul><li>Privacy Policy</li><li>Terms &amp; Conditions</li><li>Shipping Policy</li><li>FAQ's</li><li>Sitemap</li><li>Blog</li></ul>
</div>
<div class="abs footer-col" style="left:878px;top:3466px"><h3>Contact info</h3></div>
<div class="contact-item" style="left:878px;top:3518px">
  <svg width="13" height="10" viewBox="0 0 13 10"><rect width="13" height="10" fill="#c1161f"/><polyline points="0,0 6.5,5 13,0" fill="none" stroke="#fff"/></svg>
  Email:<br>info@portail-ensemble.ch
</div>
<div class="contact-item" style="left:878px;top:3574px">
  <svg width="13" height="13" viewBox="0 0 24 24"><path d="M6.6 10.8a15 15 0 006.6 6.6l2.2-2.2a1 1 0 011-.25 11 11 0 003.6.6 1 1 0 011 1V20a1 1 0 01-1 1A17 17 0 013 4a1 1 0 011-1h3.5a1 1 0 011 1 11 11 0 00.6 3.6 1 1 0 01-.25 1z" fill="#c1161f"/></svg>
  Phone:<br>CH00 4120 7733 5018 2264
</div>
<div class="contact-item" style="left:878px;top:3632px">
  <svg width="12" height="16" viewBox="0 0 12 16"><path d="M6 0a6 6 0 00-6 6c0 4.5 6 10 6 10s6-5.5 6-10a6 6 0 00-6-6zm0 8.5A2.5 2.5 0 116 3.5a2.5 2.5 0 010 5z" fill="#c1161f"/></svg>
  Location:<br>Portail Ensemble<br>Chemin des Érables 12<br>1874 Champéry
</div>

<div class="abs" style="left:89px;top:3760px;width:1022px;height:1px;background:#46525b"></div>
<p class="abs copyright">© COPYRIGHT 2022 PORTAIL ENSEMBLE, ALL RIGHTS RESERVED</p>
<div class="abs" style="left:1133px;top:3762px;width:40px;height:40px;border-radius:50%;background:var(--red)">
  <svg width="40" height="40" viewBox="0 0 40 40"><polyline points="15,21 20,16 25,21" fill="none" stroke="#fff" stroke-width="1.5"/><line x1="20" y1="16" x2="20" y2="26" stroke="#fff" stroke-width="1.5"/></svg>
</div>

</body>
</html>
```